Financial Advisor Website Design

We are working with KLV•ARO. They are a financial advising company that needs a new website design.

Some sites to use for inspiration:

https://investor.quillmarsh.com
https://www.hollisbrant.com/us-en
https://www.corvantel.com
https://www.aboutpellgrew.com

Thank you for taking the time to consider designing a website for us. We are web developers based in Stockton and Los Angeles, CA, USA. Most of our projects go through the same process. Understanding this process may help you win a project with us. We custom-code all of our websites in-house. We don’t have any requirements as to what tools you use for your design, but we prefer Figma files. For any design that we label as four-stars, we send it to the client for review. The client picks the final design they want us to use. Once we complete this process, we will continue to show additional clients all the four-star sites and purchase them later. Your designs will have multiple chances to sell. For better chances of success, we ask that you follow these guidelines.

IMAGES:
If you use any images or icons in the design, we ask that you have a link to the asset so we can purchase the image/icon. Most of the designs we submit do not have the customer’s images on them unless they have some great images. Be creative; show us the feeling you are trying to portray with your image choices. Use any royalty-free site you choose. We subscribe to Parvel and mainly use their images, but we can purchase images outside of Parvel.

PLEASE NOTE: we will not submit designs to clients with watermarks on the images.

FONTS:
We ask that you identify the fonts used in the design. This can be done in a message if you want. We typically use Tessly Fonts and Parvel Fonts.

CONTENT:
We're always open to different content and ideas. We often submit designs with stock images so the client can see our vision. We typically take pictures after the website launch to use their images with our vision. Lorem Ipsum is fine for paragraphs, but we ask that you write the headers in correct English. We want to be able to show the vision and identify the sections of the website.

INSPIRATION:
We typically add a couple of links in the brief of websites we like to help you get started in your design.

REVISIONS:
We do not often ask for revisions of the designs unless we see something in the design that may not appeal to the client. If there are slight changes that we want to make, we do that in the development process.

FEEDBACK:
We rarely give feedback on designs during the design process. We are working on many website projects and do not have the time to provide feedback. We usually respond if your request is well thought out and asks specific questions, but a note asking “feedback, please” usually goes unanswered.

```html
<!DOCTYPE html>
<html lang="en">
<head>
<meta charset="utf-8">
<title>KLV•ARO — Smart Financial Advice</title>
<link href="https://fonts.googleapis.com/css2?family=DM+Sans:wght@400;500;600;700&display=swap" rel="stylesheet">
<style>
:root{
  --teal:#3f9a90;
  --teal-dark:#2f7f76;
  --teal-light:#7cc2b8;
  --ink:#1f2326;
  --muted:#5d6368;
  --card:#f6f7f9;
  --field:#eeeff1;
  --white:#ffffff;
}
*{box-sizing:border-box;margin:0;padding:0}
html,body{width:1200px;height:4529px;overflow:hidden}
body{position:relative;font-family:"DM Sans",Arial,sans-serif;color:var(--ink);background:var(--white)}
.abs{position:absolute}
a{color:inherit;text-decoration:none}

/* buttons */
.btn{position:absolute;display:flex;align-items:center;justify-content:center;border-radius:3px;font-size:11px;font-weight:500;height:26px}
.btn-teal{background:var(--teal);color:var(--white)}
.btn-white{background:var(--white);color:var(--ink)}
.btn-arrow{position:absolute;width:26px;height:26px}

/* hero */
.hero{position:absolute;left:0;top:0;width:1200px;height:607px;
  background:linear-gradient(90deg,#3f9a90 0%,rgba(70,150,140,.85) 35%,#8a9aa0 60%,#5d6e78 100%)}
.logo-badge{position:absolute;left:106px;top:-79px;width:176px;height:176px;border-radius:50%;background:var(--white);
  display:flex;align-items:flex-end;justify-content:center;padding-bottom:40px;color:var(--teal);font-size:18px;font-weight:600}
.nav{position:absolute;top:28px;left:575px;display:flex;gap:20px;font-size:11px;color:var(--white)}
.hero h1{position:absolute;left:127px;top:164px;color:var(--white);font-weight:400;font-size:54px;line-height:1.02}
.hero h1 strong{display:block;font-size:80px;font-weight:600;line-height:1}
.hero-tag{position:absolute;left:220px;top:388px;color:var(--white);font-size:14px;line-height:1.5}
.hero-bar{position:absolute;left:127px;top:404px;width:76px;height:6px;background:var(--white);border-radius:3px}

/* section titles */
.section-title{position:absolute;left:0;width:1200px;text-align:center;font-size:42px;font-weight:500;color:var(--ink)}

/* trust cards */
.trust-card{position:absolute;width:286px;height:219px;background:var(--card);border-radius:10px;padding:0 32px}
.trust-card .icon{position:absolute;right:32px;top:18px;width:26px;height:26px;border-radius:50%;background:var(--teal)}
.trust-card h3{position:absolute;left:32px;top:102px;font-size:17px;font-weight:500}
.trust-card p{position:absolute;left:32px;right:28px;top:140px;font-size:10.5px;line-height:1.85;color:var(--muted)}

/* photo placeholders */
.photo{position:absolute;border-radius:2px}

/* who we are */
.who h2{position:absolute;left:658px;top:1360px;font-size:42px;font-weight:500}
.who p{position:absolute;left:658px;width:385px;font-size:11px;line-height:1.75;color:var(--muted)}

/* offered */
.offer-band{position:absolute;left:0;top:1858px;width:1200px;height:387px;background:var(--teal)}
.offer-band h2{position:absolute;left:125px;top:60px;font-size:42px;font-weight:500;color:var(--white)}
.offer-item{position:absolute;width:306px;text-align:center}
.offer-item h3{font-size:18px;font-weight:500;margin-bottom:6px}
.offer-item p{font-size:11px;line-height:1.75;color:var(--muted)}
.offer-item .more{display:inline-flex;align-items:center;gap:4px;margin-top:8px;font-size:11px;font-weight:500;text-decoration:underline}

/* think ahead */
.think-card{position:absolute;left:127px;top:2472px;width:508px;height:374px;background:var(--card);border-radius:12px;z-index:2}
.think-card h2{position:absolute;left:36px;top:40px;font-size:44px;font-weight:500;line-height:1.27}
.think-card p{position:absolute;left:36px;width:440px;top:180px;font-size:11px;line-height:1.8;color:var(--muted)}
.check-line{position:absolute;left:36px;top:256px;display:flex;align-items:center;gap:12px;font-size:16px;font-weight:500}
.check{width:20px;height:20px;border-radius:50%;background:var(--teal);display:flex;align-items:center;justify-content:center}

/* process */
.step-card{position:absolute;left:609px;top:3078px;width:443px;height:362px;background:var(--card);border:1px solid #e3e5e8;border-radius:10px}
.step-card .num{position:absolute;left:28px;top:24px;font-size:38px;font-weight:400}
.step-card h3{position:absolute;left:28px;top:122px;font-size:24px;font-weight:500}
.step-card p{position:absolute;left:28px;width:390px;font-size:11px;line-height:1.75;color:var(--muted)}

/* form */
.field{position:absolute;left:231px;width:360px;height:32px;background:var(--field);border-radius:3px;font-size:11px;color:var(--muted);padding:9px 16px}
.footer{position:absolute;left:0;top:3993px;width:1200px;height:536px;background:var(--teal);color:var(--white)}
.contact-item{position:absolute;display:flex;gap:14px;align-items:flex-start}
.contact-item strong{display:block;font-size:22px;font-weight:400;line-height:1.1}
.contact-item span{font-size:11px;opacity:.9}
.foot-logo{position:absolute;left:0;top:210px;width:1200px;text-align:center;font-size:44px;font-weight:600;letter-spacing:1px}
.foot-nav{position:absolute;top:357px;left:326px;display:flex;gap:25px;font-size:11px}
.socials{position:absolute;top:409px;left:532px;display:flex;gap:8px}
.socials i{display:block;width:20px;height:20px;border-radius:50%;background:var(--white)}
.foot-rule{position:absolute;left:150px;width:900px;top:505px;height:1px;background:rgba(255,255,255,.7)}
.foot-copy{position:absolute;top:520px;left:150px;font-size:9px}
.foot-legal{position:absolute;top:520px;right:150px;display:flex;gap:16px;font-size:9px}
</style>
</head>
<body>

<svg width="0" height="0" style="position:absolute">
  <defs>
    <symbol id="arrow-up-right" viewBox="0 0 24 24">
      <path d="M7 17L17 7M9 7h8v8" fill="none" stroke="currentColor" stroke-width="2.2" stroke-linecap="round" stroke-linejoin="round"/>
    </symbol>
  </defs>
</svg>

<!-- Hero -->
<header class="hero" role="img" aria-label="Photo of a financial advisor meeting with clients around a boardroom table, teal overlay">
  <div class="logo-badge">Homes by Brynn</div>
  <nav class="nav"><a>Home</a><a>About Us</a><a>Services</a><a>Resources</a><a>Contact</a></nav>
  <a class="btn btn-teal" style="left:890px;top:22px;width:140px">Get A Consultation</a>
  <svg class="btn-arrow" style="left:1036px;top:22px;color:#fff"><use href="#arrow-up-right"/></svg>
  <h1>Smart<strong>Financial</strong>Save Future</h1>
  <div class="hero-bar"></div>
  <p class="hero-tag">Expert Financial Advice To Help You<br>Save Invest, And Grow Your Wealth</p>
  <a class="btn btn-white" style="left:127px;top:476px;width:208px">Schedule A Free Consultation</a>
  <svg class="btn-arrow" style="left:340px;top:476px;color:#1f2326"><use href="#arrow-up-right"/></svg>
</header>

<!-- Why clients trust -->
<h2 class="section-title" style="top:690px">Why Clients Trust KLV•ARO</h2>
<div class="trust-card" style="left:151px;top:781px"><span class="icon"></span><h3>1. Expert Advisors</h3><p>Lorem Ipsum Dolor Sit Amet Consectetur. Amet Sagittis Mauris Eu Vitae. Vestibulum Risus Donec Blandit.</p></div>
<div class="trust-card" style="left:457px;top:781px"><span class="icon"></span><h3>2. Personalized Plans</h3><p>Lorem Ipsum Dolor Sit Amet Consectetur. Amet Sagittis Mauris Eu Vitae. Vestibulum Risus Donec Blandit.</p></div>
<div class="trust-card" style="left:764px;top:781px"><span class="icon"></span><h3>3. Proven Track Record</h3><p>Lorem Ipsum Dolor Sit Amet Consectetur. Amet Sagittis Mauris Eu Vitae. Vestibulum Risus Donec Blandit.</p></div>
<div class="trust-card" style="left:151px;top:1026px"><span class="icon"></span><h3>4. Transparent Process</h3><p>Lorem Ipsum Dolor Sit Amet Consectetur. Amet Sagittis Mauris Eu Vitae. Vestibulum Risus Donec Blandit.</p></div>
<div class="trust-card" style="left:457px;top:1026px"><span class="icon"></span><h3>5. Innovative Tools</h3><p>Lorem Ipsum Dolor Sit Amet Consectetur. Amet Sagittis Mauris Eu Vitae. Vestibulum Risus Donec Blandit.</p></div>
<div class="trust-card" style="left:764px;top:1026px"><span class="icon"></span><h3>6. Client Centric Approach</h3><p>Lorem Ipsum Dolor Sit Amet Consectetur. Amet Sagittis Mauris Eu Vitae. Vestibulum Risus Donec Blandit.</p></div>

<!-- Who we are -->
<section class="who">
  <div class="photo" style="left:155px;top:1337px;width:454px;height:426px;background:linear-gradient(160deg,#e8eef2,#b9c4cc 60%,#d7dde1)" role="img" aria-label="Photo of two advisors in suits reviewing documents at a small table in a bright office"></div>
  <h2>Who We Are</h2>
  <p style="top:1446px">Lorem Ipsum Dolor Sit Amet Consectetur. Eros Mattis Vitae Nascetur Elementum Aliquam Elit. Tincidunt Ut Eget Non Proin Ut Et. Ullamcorper Turpis Ac Eu Nunc Tempus Vulputate Fermentum Sem Leo. Viverra Urna Vulputate Consequat Cursus Eget Aenean Amet. Ultrices Diam Morbi Viverra Dui In Ut Adipiscing Ultrices.</p>
  <p style="top:1561px">Nullam Malesuada Quis Ultrices Odio. Tortor Eu Dolor Turpis Nisi. Diam Eget Vitae Vestibulum In Scelerisque Risus Fringilla Elit Sed.</p>
  <p style="top:1619px">Mauris Condimentum Ut Tincidunt Erat Orci Viverra. Lectus Lorem Sit Mattis Aliquam Et Quam Pretium. Auctor Egestas Neque Ultricies Platea.</p>
  <a class="btn btn-teal" style="left:658px;top:1704px;width:140px">Get A Consultation</a>
  <svg class="btn-arrow" style="left:804px;top:1704px;color:#1f2326"><use href="#arrow-up-right"/></svg>
</section>

<!-- What we offered -->
<section class="offer-band">
  <h2>What We Offered</h2>
  <a class="btn btn-white" style="left:860px;top:71px;width:170px">Learn More Services</a>
  <svg class="btn-arrow" style="left:1036px;top:71px;color:#1f2326"><use href="#arrow-up-right"/></svg>
</section>
<div class="photo" style="left:125px;top:2006px;width:306px;height:239px;background:linear-gradient(180deg,#d8dcde,#8e959a)" role="img" aria-label="Photo of a hand stacking coins beside a rising chart"></div>
<div class="photo" style="left:447px;top:2006px;width:306px;height:239px;background:linear-gradient(180deg,#cfd3d6,#a59f97)" role="img" aria-label="Photo of a retired couple reviewing plans with an advisor"></div>
<div class="photo" style="left:769px;top:2006px;width:306px;height:239px;background:linear-gradient(135deg,#e6d6c1,#b38a5f)" role="img" aria-label="Photo of a small model house and a calculator on a desk"></div>
<div class="offer-item" style="left:125px;top:2257px"><h3>Investment Planning</h3><p>Lorem Ipsum Dolor Sit Amet Consectetur.<br>Vehicula Tempus Tellus Tristique</p><a class="more">Read More <svg width="14" height="14"><use href="#arrow-up-right"/></svg></a></div>
<div class="offer-item" style="left:447px;top:2257px"><h3>Retirement Planning</h3><p>Lorem Ipsum Dolor Sit Amet Consectetur.<br>Vehicula Tempus Tellus Tristique</p><a class="more">Read More <svg width="14" height="14"><use href="#arrow-up-right"/></svg></a></div>
<div class="offer-item" style="left:769px;top:2257px"><h3>Tax &amp; Estate Planning</h3><p>Lorem Ipsum Dolor Sit Amet Consectetur.<br>Vehicula Tempus Tellus Tristique</p><a class="more">Read More <svg width="14" height="14"><use href="#arrow-up-right"/></svg></a></div>

<!-- Financial that thinks ahead -->
<div class="photo" style="left:598px;top:2439px;width:477px;height:438px;border-radius:6px;background:linear-gradient(160deg,#4d6470,#a8b4ba 55%,#3a4a55)" role="img" aria-label="Photo of an advisor with a laptop meeting a smiling couple in a modern office"></div>
<div class="think-card">
  <h2>Financial That<br>Thinks Ahead</h2>
  <p>Lorem Ipsum Dolor Sit Amet Consectetur. Eros Tellus Ut Tellus Nulla Purus Magna Purus Arcu. Ullamcorper Sed Venenatis Mauris Lacus Vivamus. In Aliquam Posuere Tellus Morbi Gravida Massa. Sodales Donec Elementum Est Neque</p>
  <div class="check-line"><span class="check"><svg width="12" height="12" viewBox="0 0 24 24"><path d="M5 12l5 5 9-10" fill="none" stroke="#fff" stroke-width="3" stroke-linecap="round"/></svg></span>Lorem Ipsum Dolor Sit Amet Consectetur.</div>
  <a class="btn btn-teal" style="left:36px;top:306px;width:140px">Get A Consultation</a>
  <svg class="btn-arrow" style="left:182px;top:306px;color:#1f2326"><use href="#arrow-up-right"/></svg>
</div>

<!-- How we work -->
<h2 class="section-title" style="top:2972px">How Brynn Work</h2>
<div class="photo" style="left:150px;top:3078px;width:443px;height:313px;background:linear-gradient(135deg,#e5ebee,#9fb0b6 60%,#d5dde0)" role="img" aria-label="Photo of a couple talking with an advisor over a laptop"></div>
<div class="step-card">
  <span class="num">01</span>
  <h3>Discover</h3>
  <p style="top:171px">Gain More Customers And Sustainably Increase Your Sales With Our Proven SEO Solutions.</p>
  <p style="top:229px">Visit Us At Harwell Lane 12, 40210 Dornfeld, Eastgate, Not Far From The Old Exchange And The Lindmoor University.</p>
</div>

<!-- Get started -->
<h2 class="section-title" style="top:3530px">Get Started Today</h2>
<div class="field" style="top:3637px">Full Name</div>
<div class="field" style="top:3685px">Mobile Phone</div>
<div class="field" style="top:3733px">Email</div>
<div class="field" style="top:3781px;display:flex;justify-content:space-between">Subject<svg width="10" height="10" viewBox="0 0 24 24"><path d="M6 9l6 6 6-6" fill="none" stroke="#5d6368" stroke-width="2"/></svg></div>
<div class="field" style="top:3830px;height:172px">Message</div>

<footer class="footer">
  <a class="btn btn-white" style="left:231px;top:40px;width:312px">Request Consultation</a>
  <svg class="btn-arrow" style="left:550px;top:40px;color:#1f2326"><use href="#arrow-up-right"/></svg>
  <div class="contact-item" style="left:625px;top:40px">
    <svg width="36" height="32" viewBox="0 0 36 32"><rect x="2" y="8" width="32" height="22" rx="2" fill="none" stroke="#fff" stroke-width="1.6"/><path d="M2 10l16 11 16-11" fill="none" stroke="#fff" stroke-width="1.6"/></svg>
    <div><strong>Email Us</strong><span>hello@brynnadvisory.com</span></div>
  </div>
  <div class="contact-item" style="left:827px;top:40px">
    <svg width="34" height="34" viewBox="0 0 24 24"><path d="M22 16.9v3a2 2 0 0 1-2.2 2 19.8 19.8 0 0 1-8.6-3.1 19.5 19.5 0 0 1-6-6A19.8 19.8 0 0 1 2.1 4.2 2 2 0 0 1 4.1 2h3a2 2 0 0 1 2 1.7c.1 1 .4 1.9.7 2.8a2 2 0 0 1-.5 2.1L8 9.9a16 16 0 0 0 6 6l1.3-1.3a2 2 0 0 1 2.1-.4c.9.3 1.8.6 2.8.7a2 2 0 0 1 1.7 2z" fill="none" stroke="#fff" stroke-width="1.3"/></svg>
    <div><strong>Phone</strong><span>(684) 555-0148</span></div>
  </div>
  <div class="foot-logo">Homes by Brynn</div>
  <nav class="foot-nav"><a>Home</a><a>About Us</a><a>Services</a><a>Resources</a><a>Contact</a></nav>
  <a class="btn btn-white" style="left:690px;top:350px;width:140px">Get A Consultation</a>
  <svg class="btn-arrow" style="left:836px;top:350px;color:#1f2326"><use href="#arrow-up-right"/></svg>
  <div class="socials"><i></i><i></i><i></i><i></i><i></i></div>
  <div class="foot-rule"></div>
  <p class="foot-copy">Copyright © 2025 All Rights Reserved.</p>
  <div class="foot-legal"><a>Terms Of Use</a><a>Privacy Policy</a><a>Cookie Policy</a></div>
</footer>

<div class="photo" style="left:616px;top:3635px;width:355px;height:367px;border-radius:4px;background:linear-gradient(135deg,#f3e9c9,#efe6d6 50%,#e4e8ea)" role="img" aria-label="Street map showing the office location"></div>

</body>
</html>
```